Updated DJ business Card showing other businesses

DJ Kestro offers professional mobile dj services including DJ. MC. Karaoke.
Silent Disco (will attach logo)
I also offer a 360 Photo Booth.

Contact info:
(555) 314-7720
lenny.corbitt@mailvane.net
Social Media @DJKestroBPZ

```html
<!DOCTYPE html>
<html lang="en">
<head>
<meta charset="utf-8">
<title>DJ Kestro – Business Card</title>
<link rel="stylesheet" href="https://fonts.googleapis.com/css2?family=Montserrat:wght@400;500;600;800&display=swap">
<style>
  :root {
    --backdrop: #b3b3b3;
    --paper: #ffffff;
    --ink: #000000;
    --record-grey: #808080;
    --label-red: #d4214a;
    --text-dark: #111111;
  }
  * { margin: 0; padding: 0; box-sizing: border-box; }
  html, body {
    width: 1000px;
    height: 1200px;
    overflow: hidden;
    background: var(--backdrop);
    font-family: "Montserrat", sans-serif;
  }
  .card {
    position: absolute;
    left: 50px;
    width: 899px;
    height: 540px;
    background: var(--paper);
    overflow: hidden;
  }
  .card--front { top: 43px; }
  .card--back { top: 612px; }
  .card__art {
    position: absolute;
    inset: 0;
    width: 899px;
    height: 540px;
  }

  /* Front */
  .brand-name {
    position: absolute;
    left: 67px;
    top: 70px;
    font-weight: 800;
    font-size: 64px;
    letter-spacing: 1px;
    color: var(--label-red);
    line-height: 1;
  }
  .contact {
    position: absolute;
    left: 74px;
    top: 343px;
    list-style: none;
    font-weight: 400;
    font-size: 30px;
    line-height: 47px;
    color: var(--text-dark);
    letter-spacing: 0.3px;
  }

  /* Back */
  .back-title {
    position: absolute;
    left: 67px;
    top: 50px;
    font-weight: 500;
    font-size: 35px;
    color: var(--paper);
    line-height: 1;
  }
  .service-band {
    position: absolute;
    display: flex;
    align-items: center;
    height: 50px;
    background: var(--ink);
    color: var(--paper);
    font-weight: 600;
    font-size: 25px;
    letter-spacing: 0.6px;
    white-space: nowrap;
  }
  .service-band--intro { left: 0; top: 97px; width: 792px; padding-left: 128px; }
  .service-band--acts { left: 288px; top: 183px; width: 611px; padding-left: 204px; }
  .service-band--booth { left: 263px; top: 436px; width: 636px; padding-left: 218px; }

  .feature-mark {
    position: absolute;
    left: 462px;
    top: 300px;
    display: flex;
    align-items: center;
    gap: 14px;
  }
  .feature-mark__dot {
    width: 56px;
    height: 56px;
    border-radius: 50%;
    background: var(--ink);
  }
  .feature-mark__name {
    font-weight: 800;
    font-size: 40px;
    color: var(--ink);
    letter-spacing: 0.5px;
    white-space: nowrap;
  }
</style>
</head>
<body>

<section class="card card--front" aria-label="Card front">
  <svg class="card__art" viewBox="0 0 899 540" aria-hidden="true">
    <circle cx="981" cy="270" r="448" fill="var(--record-grey)"/>
    <circle cx="981" cy="270" r="381" fill="var(--ink)"/>
    <circle cx="981" cy="270" r="203" fill="var(--label-red)"/>
  </svg>
  <div class="brand-name">DJ Kestro</div>
  <ul class="contact">
    <li>(555) 314-7720</li>
    <li>lenny.corbitt@mailvane.net</li>
    <li>Social Media @DJKestroBPZ</li>
  </ul>
</section>

<section class="card card--back" aria-label="Card back">
  <svg class="card__art" viewBox="0 0 899 540" aria-hidden="true">
    <circle cx="-81" cy="270" r="448" fill="var(--record-grey)"/>
    <circle cx="-81" cy="270" r="381" fill="var(--ink)"/>
    <circle cx="-81" cy="270" r="203" fill="var(--label-red)"/>
  </svg>
  <h1 class="back-title">DJ Kestro</h1>
  <div class="service-band service-band--intro">OFFERS PROFESSIONAL MOBILE DJ SERVICES</div>
  <div class="service-band service-band--acts">DJ. MC. KARAOKE.</div>
  <div class="feature-mark">
    <span class="feature-mark__dot" aria-hidden="true"></span>
    <span class="feature-mark__name">Silent Disco</span>
  </div>
  <div class="service-band service-band--booth">360 PHOTO BOOTH.</div>
</section>

</body>
</html>
```